Whitmore Properties
business cards, stationery
Can you please extend the contest ....
can you please extend the contest?
@vElpo - we like the black and gold card in #16 but do not like the gold and white stationary. We would like more black in the stationary with gold being the accent with more focus at the top of the stationary.
The font used in our logo is "Trajanpro" both regular and bold.
kindly tell the font name which is used in your logo ...

```html
<!DOCTYPE html>
<html lang="en">
<head>
<meta charset="utf-8">
<title>Whitmore Properties — Stationery Set</title>
<link href="https://fonts.googleapis.com/css2?family=Cinzel:wght@400;700&family=Open+Sans:wght@400;600&display=swap" rel="stylesheet">
<style>
  :root{
    --backdrop:#e6e4e0;
    --paper:#ffffff;
    --charcoal:#2b2b2b;
    --graphite:#4a4a4a;
    --orange:#f28a1a;
    --orange-deep:#e0620c;
    --text-grey:#6d6d6d;
    --rule:#d9d9d9;
  }
  *{box-sizing:border-box;margin:0;padding:0}
  html,body{width:1200px;height:658px;overflow:hidden}
  body{background:var(--backdrop);position:relative;font-family:"Open Sans",Arial,sans-serif;color:var(--text-grey)}
  .sheet{position:absolute;background:var(--paper);overflow:hidden;box-shadow:0 3px 8px rgba(0,0,0,.25)}
  .sheet svg.wave{position:absolute;left:0;width:100%}
  .brand{position:absolute;display:flex;align-items:center;gap:5px}
  .brand-mark{width:12px;height:12px;background:var(--charcoal)}
  .brand-name{font-family:"Cinzel",Georgia,serif;font-weight:700;color:var(--charcoal);letter-spacing:.5px;line-height:1}
  .brand-tag{font-size:4.5px;color:var(--text-grey);margin-top:2px;letter-spacing:.3px}
  .fine{font-size:4.6px;line-height:1.7;color:var(--text-grey)}

  /* letterhead */
  .letterhead{left:180px;top:19px;width:377px;height:598px}
  .letterhead .brand{left:24px;top:50px}
  .letterhead .brand-name{font-size:15px}
  .letterhead .footer-rule{position:absolute;left:24px;right:24px;bottom:36px;height:1px;background:var(--rule)}
  .letterhead .footer{position:absolute;left:24px;right:24px;bottom:14px;text-align:center}

  /* business card front */
  .card-front{left:610px;top:46px;width:172px;height:98px}
  .card-front .brand{left:10px;top:26px}
  .card-front .brand-mark{width:9px;height:9px}
  .card-front .brand-name{font-size:9px}
  .card-front .person{position:absolute;right:10px;top:52px;text-align:right}
  .card-front .person-name{font-size:6px;font-weight:600;color:var(--orange-deep);letter-spacing:.3px}
  .card-front .contact{position:absolute;left:10px;top:52px}

  /* business card backs */
  .card-back-dark{left:792px;top:46px;width:192px;height:98px;background:radial-gradient(circle at 55% 45%,#4d4d4d,#262626)}
  .card-back-orange{left:590px;top:156px;width:173px;height:96px;background:radial-gradient(circle at 50% 45%,#f7a63a,var(--orange-deep))}
  .centered-brand{position:absolute;inset:0;display:flex;align-items:center;justify-content:center;gap:5px}
  .centered-brand .brand-mark{background:#fff;width:9px;height:9px}
  .centered-brand .brand-name{color:#fff;font-size:10px}

  /* envelopes */
  .envelope-back{left:581px;top:389px;width:211px;height:240px}
  .envelope-front{left:763px;top:336px;width:437px;height:293px}
  .envelope-front .brand{left:20px;top:62px}
  .envelope-front .brand-name{font-size:13px}
  .envelope-front .return-address{position:absolute;left:20px;top:86px}
</style>
</head>
<body>

<section class="sheet letterhead" aria-label="Letterhead">
  <svg class="wave" style="top:0" viewBox="0 0 377 60" height="60" preserveAspectRatio="none" aria-hidden="true">
    <path d="M377 0 H150 C210 18 290 28 377 22 Z" fill="var(--charcoal)"/>
    <path d="M140 0 C215 26 300 34 377 28" stroke="var(--orange)" stroke-width="3" fill="none"/>
    <path d="M160 0 C225 30 305 40 377 36" stroke="var(--graphite)" stroke-width="1.2" fill="none"/>
  </svg>
  <div class="brand">
    <span class="brand-mark"></span>
    <div>
      <div class="brand-name">WHITMORE PROPERTIES</div>
      <div class="brand-tag">Building lasting value</div>
    </div>
  </div>
  <div class="footer-rule"></div>
  <div class="footer fine">
    1200 Harbor View Lane, Suite 4, Riverton, CA 90210<br>
    (555) 014-2290 &nbsp;|&nbsp; (555) 014-2291 &nbsp;|&nbsp; info@whitmoreprops.com
  </div>
</section>

<section class="sheet card-front" aria-label="Business card front">
  <svg class="wave" style="top:0" viewBox="0 0 172 24" height="24" preserveAspectRatio="none" aria-hidden="true">
    <path d="M0 0 H172 V8 C120 18 60 16 0 6 Z" fill="var(--charcoal)"/>
    <path d="M0 9 C60 19 120 21 172 11" stroke="var(--orange)" stroke-width="2" fill="none"/>
  </svg>
  <div class="brand">
    <span class="brand-mark"></span>
    <span class="brand-name">WHITMORE</span>
  </div>
  <div class="person">
    <div class="person-name">JORDAN HALE</div>
    <div class="fine">Sales Director</div>
  </div>
  <div class="contact fine">
    1200 Harbor View Lane<br>
    (555) 014-2290<br>
    info@whitmoreprops.com
  </div>
</section>

<section class="sheet card-back-dark" aria-label="Business card back">
  <div class="centered-brand"><span class="brand-mark"></span><span class="brand-name">WHITMORE</span></div>
</section>

<section class="sheet card-back-orange" aria-label="Business card back, orange">
  <div class="centered-brand"><span class="brand-mark"></span><span class="brand-name">WHITMORE</span></div>
</section>

<section class="sheet envelope-back" aria-label="Envelope back">
  <svg viewBox="0 0 211 240" width="211" height="240" preserveAspectRatio="none" aria-hidden="true" style="position:absolute;inset:0">
    <path d="M0 0 H211 V40 C140 90 70 90 0 60 Z" fill="var(--charcoal)"/>
    <path d="M0 64 C70 94 140 94 211 44" stroke="var(--orange)" stroke-width="2.5" fill="none"/>
    <path d="M0 240 H211 V190 C140 150 70 160 0 185 Z" fill="var(--charcoal)"/>
    <path d="M0 181 C70 156 140 146 211 186" stroke="var(--orange)" stroke-width="2.5" fill="none"/>
  </svg>
</section>

<section class="sheet envelope-front" aria-label="Envelope front">
  <svg viewBox="0 0 437 293" width="437" height="293" preserveAspectRatio="none" aria-hidden="true" style="position:absolute;inset:0">
    <path d="M0 0 H437 V40 C300 60 150 40 0 15 Z" fill="var(--charcoal)"/>
    <path d="M0 20 C150 46 300 66 437 46" stroke="var(--orange)" stroke-width="3" fill="none"/>
    <path d="M0 293 H437 V240 C300 215 150 250 0 262 Z" fill="var(--charcoal)"/>
    <path d="M0 256 C150 244 300 208 437 234" stroke="var(--orange)" stroke-width="3" fill="none"/>
  </svg>
  <div class="brand">
    <span class="brand-mark"></span>
    <div class="brand-name">WHITMORE PROPERTIES</div>
  </div>
  <div class="return-address fine">
    1200 Harbor View Lane, Suite 4<br>
    Riverton, CA 90210
  </div>
</section>

</body>
</html>
```